Lumo Cellar Traders needs a new business card design

Colour theme: Gold + Red preferred
Front side: Main logo with my details as below;
Back side: Theme of some wine glasses or bottles, maybe different color of log together
Lumo Cellar Traders

Leo Park
박 성민 (this is Korean character) on the English typying board: qkr tjdals
Managing Director

Suite 7/5 Harlow Rd
Bayfield WA 6923
Tel) +61(8) 6027 3518
Mob) +61(412) 305 276

leo.park@lumocellartraders.example
lumocellar@lumocellartraders.example
www.lumocellartraders.example

Target Market(s)

Asian Market

Industry/Entity Type

Business

Contact Information for Business Card

Lumo Cellar Traders

Leo Park
박 성민 (this is Korean character) English typying: qkr tjdals
Managing Director

Suite 7/5 Harlow Rd
Bayfield WA 6923
Tel) +61(8) 6027 3518
Mob) +61(412) 305 276

Font styles to use
Serif
Decorative

Colors
ec1f27
f78f21
f04a50
faa54b
cadf82
abd036

Requirements
Must have
• Company Logo & wine theme
Nice to have
• Very simple & modern
Should not have
• No Red Color on the name of Leo Park or 박 성민
• No traditional looking. young and modern look preferred

```html
<!DOCTYPE html>
<html lang="en">
<head>
<meta charset="utf-8">
<title>Lumo Cellar Traders – Business Card</title>
<link rel="stylesheet" href="https://fonts.googleapis.com/css2?family=Exo+2:ital,wght@0,400;0,500;0,600;1,500&family=Noto+Sans+KR:wght@400&display=swap">
<style>
  :root {
    --bg: #2a2a2c;
    --card-white: #ffffff;
    --red: #e0302a;
    --red-deep: #c8211d;
    --gold: #c9a03a;
    --gold-dark: #b58a26;
    --text-grey: #555555;
    --orange-a: #e24e1f;
    --orange-b: #f27a2a;
    --orange-c: #f5a23c;
  }
  * { margin: 0; padding: 0; box-sizing: border-box; }
  html, body { width: 1200px; height: 1200px; overflow: hidden; }
  body {
    background: var(--bg);
    font-family: "Exo 2", sans-serif;
    display: flex; flex-direction: column; align-items: center; justify-content: space-evenly;
  }
  .card {
    position: relative; width: 910px; height: 520px; overflow: hidden;
    box-shadow: 0 12px 30px rgba(0,0,0,.45);
  }
  .card-front { background: var(--card-white); }
  .card-back {
    background: linear-gradient(135deg, var(--orange-a) 0%, var(--orange-b) 50%, var(--orange-c) 100%);
    display: flex; align-items: center; justify-content: center;
  }
  .front-bands { position: absolute; inset: 0; }

  .brand { position: absolute; left: 250px; top: 52px; display: flex; align-items: center; gap: 16px; }
  .brand-dot { width: 60px; height: 60px; border-radius: 50%; background: var(--red); flex: none; }
  .brand-name { font-size: 40px; font-weight: 600; color: var(--red); letter-spacing: 1px; line-height: 1; }
  .brand-tagline {
    position: absolute; left: 326px; top: 104px;
    font-size: 16px; font-weight: 500; color: var(--gold-dark); letter-spacing: .3px;
  }

  .person { position: absolute; left: 110px; top: 170px; }
  .person-name { font-size: 42px; font-weight: 500; color: var(--gold); letter-spacing: .5px; line-height: 1.1; }
  .person-korean { margin-top: 8px; font-size: 19px; color: var(--text-grey); }
  .person-korean .hangul { font-family: "Noto Sans KR", sans-serif; }
  .person-role { margin-top: 4px; font-size: 19px; color: var(--text-grey); }

  .contact { position: absolute; right: 40px; top: 190px; list-style: none; text-align: right; }
  .contact li {
    display: flex; justify-content: flex-end; align-items: center; gap: 12px;
    font-size: 19px; color: var(--text-grey); line-height: 34px;
  }
  .contact svg { width: 20px; height: 20px; flex: none; }

  .website {
    position: absolute; right: 44px; bottom: 24px;
    font-size: 28px; font-weight: 500; font-style: italic; color: #fff; letter-spacing: .5px;
  }

  .back-brand { display: flex; align-items: center; gap: 18px; }
  .back-brand .brand-dot { background: #ffffff; width: 54px; height: 54px; }
  .back-brand .brand-name { color: #ffffff; font-size: 44px; }
</style>
</head>
<body>

  <section class="card card-front" aria-label="Business card front">
    <svg class="front-bands" viewBox="0 0 910 520" aria-hidden="true">
      <polygon points="0,292 0,310 560,520 510,520" fill="var(--gold)"/>
      <polygon points="0,328 430,452 910,452 910,520 0,520" fill="var(--red)"/>
      <polygon points="0,356 330,452 0,452" fill="var(--red-deep)" opacity=".35"/>
    </svg>

    <div class="brand">
      <span class="brand-dot"></span>
      <span class="brand-name">LUMO CELLAR TRADERS</span>
    </div>
    <div class="brand-tagline">Pour, Pair &amp; Grow Your Trade</div>

    <div class="person">
      <div class="person-name">LEO PARK</div>
      <div class="person-korean"><span class="hangul">박 성민</span> - qkr tjdals</div>
      <div class="person-role">Managing Director</div>
    </div>

    <ul class="contact">
      <li>+61(8) 6027 3518
        <svg viewBox="0 0 24 24"><path fill="var(--red)" d="M6.6 10.8a15 15 0 0 0 6.6 6.6l2.2-2.2a1 1 0 0 1 1-.25 11 11 0 0 0 3.6.6 1 1 0 0 1 1 1V20a1 1 0 0 1-1 1A17 17 0 0 1 3 4a1 1 0 0 1 1-1h3.5a1 1 0 0 1 1 1 11 11 0 0 0 .6 3.6 1 1 0 0 1-.25 1z"/></svg></li>
      <li>lumocellar@lumocellartraders.example
        <svg viewBox="0 0 24 24"><rect x="2" y="5" width="20" height="14" rx="1" fill="var(--red)"/><path d="M2 6l10 7 10-7" fill="none" stroke="#fff" stroke-width="1.6"/></svg></li>
      <li>+61(412) 305 276
        <svg viewBox="0 0 24 24"><rect x="6" y="2" width="12" height="20" rx="2" fill="var(--red)"/><rect x="8" y="5" width="8" height="11" fill="#fff"/><circle cx="12" cy="19" r="1.2" fill="#fff"/></svg></li>
      <li>leo.park@lumocellartraders.example
        <svg viewBox="0 0 24 24"><rect x="2" y="5" width="20" height="14" rx="1" fill="var(--red)"/><path d="M2 6l10 7 10-7" fill="none" stroke="#fff" stroke-width="1.6"/></svg></li>
      <li>Suite 7/5 Harlow Rd, Bayfield WA 6923
        <svg viewBox="0 0 24 24"><path fill="var(--red)" d="M12 2a7 7 0 0 0-7 7c0 5 7 13 7 13s7-8 7-13a7 7 0 0 0-7-7zm0 9.5A2.5 2.5 0 1 1 12 6.5a2.5 2.5 0 0 1 0 5z"/></svg></li>
    </ul>

    <div class="website">www.lumocellartraders.example</div>
  </section>

  <section class="card card-back" aria-label="Business card back">
    <div class="back-brand">
      <span class="brand-dot"></span>
      <span class="brand-name">LUMO CELLAR TRADERS</span>
    </div>
  </section>

</body>
</html>
```